business card for author of crime novel

I am an author with a new book. I need a business card with the book's cover on one side (already uploaded), and contact details on the other.

Tom Velasquin
Author

telephone: 917-555-0162
website: www.tomvelasquin.example
facebook: folkbook.example/tvelasquin
twitter: chirper.example/tvelasquin
email: tvelasquin@mailbox.example

Target Market(s)

Readers of mystery books

Industry/Entity Type

Business

Contact Information for Business Card

Tom Velasquin
Author

telephone: 917-555-0162

Font styles to use
Serif
Sans Serif

Requirements
Must have
• Book cover on one side. My contact info on the other, with the name of the book repeated if that makes sense. Clean design.
Should not have
• Overly ornate, too formal, too distracting

```html
<!DOCTYPE html>
<html lang="en">
<head>
<meta charset="utf-8">
<title>Tom Velasquin – Author Business Card</title>
<link rel="stylesheet" href="https://fonts.googleapis.com/css2?family=Crimson+Text:ital,wght@0,400;0,600;1,400&family=Arimo:wght@400;700&family=Special+Elite&display=swap">
<style>
  :root {
    --stage: #2a2623;
    --gold-light: #d29d35;
    --gold: #c48b24;
    --gold-dark: #a8741a;
    --paper: #d9c296;
    --paper-edge: #f7f2e6;
    --ink: #4a3b24;
    --ink-dark: #1c1710;
    --white: #ffffff;
    --photo-light: #7f95a3;
    --photo-dark: #34444f;
    --author-yellow: #e6dc45;
    --label: #e2cfa4;
    --label-edge: #b59a68;
  }
  * { box-sizing: border-box; margin: 0; padding: 0; }
  html, body { width: 1200px; height: 556px; overflow: hidden; }
  body {
    background: var(--stage);
    display: flex;
    align-items: center;
    justify-content: center;
    gap: 48px;
  }
  .card {
    position: relative;
    width: 272px;
    height: 472px;
    overflow: hidden;
    background: linear-gradient(180deg, var(--gold-light) 0%, var(--gold) 55%, var(--gold-dark) 100%);
    box-shadow: 0 6px 18px rgba(0,0,0,.45);
  }

  /* Contact side */
  .contact-name {
    position: absolute; top: 44px; left: 0; width: 100%;
    text-align: center;
    font: 400 28px/1 "Crimson Text", Georgia, serif;
    color: var(--white);
    text-shadow: 1px 2px 3px rgba(0,0,0,.45);
  }
  .contact-role {
    position: absolute; top: 76px; left: 0; width: 100%;
    text-align: center;
    font: italic 400 11px/1 "Crimson Text", Georgia, serif;
    color: var(--white);
  }
  .torn-band { position: absolute; top: 0; left: 0; }
  .contact-phone {
    position: absolute; top: 164px; left: 0; width: 100%;
    display: flex; align-items: center; justify-content: center; gap: 6px;
    font: 700 21px/1 "Arimo", Arial, sans-serif;
    color: var(--white);
    text-shadow: 1px 1px 2px rgba(0,0,0,.45);
  }
  .contact-list {
    position: absolute; top: 200px; left: 40px;
    list-style: none;
    font: 400 12px/16px "Arimo", Arial, sans-serif;
    color: var(--ink);
  }
  .contact-list li { display: flex; align-items: center; gap: 6px; white-space: nowrap; }
  .contact-dot {
    width: 9px; height: 9px; border-radius: 50%;
    background: var(--ink);
    flex: none;
  }
  .contact-square { border-radius: 1px; }
  .book-stack {
    position: absolute; left: 46px; top: 326px;
    width: 180px; height: 126px;
    border-radius: 4px;
    background: linear-gradient(160deg, var(--photo-light) 0%, var(--photo-dark) 55%, var(--gold-dark) 100%);
    transform: rotate(-8deg);
    box-shadow: 0 6px 10px rgba(0,0,0,.35);
  }

  /* Cover side */
  .cover-title {
    position: absolute; top: 48px; left: 0; width: 100%;
    text-align: center;
    font: 400 21px/1 "Special Elite", "Courier New", monospace;
    letter-spacing: 1px;
    color: var(--ink-dark);
  }
  .cover-photo {
    position: absolute; top: 85px; left: 24px;
    width: 223px; height: 296px;
    background: radial-gradient(ellipse at 45% 35%, var(--photo-light) 0%, var(--photo-dark) 85%);
  }
  .cover-author {
    position: absolute; top: 340px; right: 34px;
    text-align: center;
    font: 400 16px/18px "Crimson Text", Georgia, serif;
    letter-spacing: .5px;
    color: var(--author-yellow);
  }
  .series-label {
    position: absolute; top: 395px; left: 24px;
    width: 226px; height: 36px;
    background: var(--label);
    border: 1px solid var(--label-edge);
    transform: rotate(-1deg);
    display: flex; align-items: center; justify-content: center;
    font: 400 17px/1 "Crimson Text", Georgia, serif;
    color: var(--ink-dark);
    box-shadow: 0 2px 3px rgba(0,0,0,.3);
  }
</style>
</head>
<body>

  <section class="card card-contact" aria-label="Contact side">
    <h1 class="contact-name">Tom Velasquin</h1>
    <p class="contact-role">Author</p>

    <svg class="torn-band" width="272" height="472" viewBox="0 0 272 472" aria-hidden="true">
      <path fill="var(--paper-edge)" d="M0 146 L14 142 L22 148 L34 140 L48 143 L58 136 L72 139 L84 131 L98 134 L110 127 L124 130 L136 123 L150 126 L162 119 L178 121 L190 114 L204 117 L218 110 L232 113 L246 106 L260 109 L272 103 L272 283 L258 286 L246 280 L232 288 L218 284 L204 291 L190 287 L176 294 L162 290 L148 297 L134 293 L120 300 L106 296 L92 303 L78 299 L64 306 L50 302 L36 309 L22 305 L10 311 L0 308 Z"/>
      <path fill="var(--paper)" d="M0 152 L12 149 L24 153 L36 146 L50 149 L60 142 L74 145 L86 137 L100 140 L112 133 L126 136 L138 129 L152 132 L164 125 L180 127 L192 120 L206 123 L220 116 L234 119 L248 112 L262 115 L272 110 L272 277 L260 280 L246 275 L232 282 L218 278 L204 285 L190 281 L176 288 L162 284 L148 291 L134 287 L120 294 L106 290 L92 297 L78 293 L64 300 L50 296 L36 303 L22 299 L10 305 L0 302 Z"/>
    </svg>

    <p class="contact-phone">
      <svg width="14" height="20" viewBox="0 0 14 20" aria-hidden="true">
        <rect x="1.5" y="1.5" width="11" height="17" rx="2" fill="none" stroke="var(--white)" stroke-width="2"/>
        <circle cx="7" cy="15" r="1.2" fill="var(--white)"/>
      </svg>
      917-555-0162
    </p>

    <ul class="contact-list">
      <li><span class="contact-dot"></span>www.tomvelasquin.example</li>
      <li><span class="contact-dot contact-square"></span>folkbook.example/tvelasquin</li>
      <li><span class="contact-dot contact-square"></span>chirper.example/tvelasquin</li>
      <li><span class="contact-dot"></span>tvelasquin@mailbox.example</li>
    </ul>

    <div class="book-stack" role="img" aria-label="Stack of copies of the novel Dead Air Alley"></div>
  </section>

  <section class="card card-cover" aria-label="Book cover side">
    <h2 class="cover-title">DEAD AIR ALLEY</h2>
    <div class="cover-photo" role="img" aria-label="Blue-toned photograph of an old brick tenement with fire escapes"></div>
    <p class="cover-author">TOM<br>VELASQUIN</p>
    <p class="series-label">A Marlowe Finch Mystery</p>
  </section>

</body>
</html>
```